Design for "Vellow" protein health bars wrappers

I need a new design for a protein bar that my partners and I are launching for the North American and European markets.
The bar's name is "Vellow."
Given the masculine/aggressive nature of that name, we are thinking of neutralizing it with a more feminine/soft font and design. But hey - the sky is the limit. We obviously want this 20-gram protein bar to sell to a wide net (not just men but women also). So if it means having a Pellam Comic font/design (or whatever) in order to do this, so be it. I leave it up to your intelligence and experience.

ADDED ON FEBRUARY 24:

The official name of the bar is just "VELLOW" (not "Vellow Protein").

We have six flavors divided into two categories, which are 1) SOFT and 2) CRUNCHY.
So, the idea is to make two similar designs for the wrapper that still distinguish themselves from each other because one is 'soft' and the other is 'crunchy.'
Then, within each category, the idea is to have three color variations, designating the three flavors in each category.

Please look at the dimensions and examples of the generic wrapper designs that we already have (and which we find too generic), which I have uploaded.

Target Market(s)

North America - Brindle, Fair Harvest
Europe - Norway, Sweden, Denmark, Germany, France, Switzerland, Italy.

Industry/Entity Type

Nutrition

Logo Text

Vellow

Font styles to use
Serif
Decorative

Colors
fff6dc
f04a50

Requirements
Must have
• The title is "Vellow".
• We have six flavors divided into two categories, which are 1) SOFT and 2) CRUNCHY.
• You can work on the two different types of similar-but-different designs for the "soft" and for the "cruncy." Then it's just a question of color variations for each flavor.
• The flavors are:
• SOFT: 1) strawberry, 2) Chocolate brownie, 3) Cinnamon Crunch
• CRUNCY: 1) Peanut, 2) Lemon, 3) Coconut.
• On the side or at the bottom, there should be stated:
• "20 gm protein"
• "children friendly"
Nice to have
• Obvious: a design that catches the eye and inspires someone to buy the bar to eat it.
• Part of the design could include a photograph of the actual bar (you can use generic photos for that until we place a pic of the actual bar). Like 1/4th of the total surface (or even a little smaller).

```html
<!DOCTYPE html>
<html lang="en">
<head>
<meta charset="utf-8">
<title>Vellow Wrappers</title>
<link href="https://fonts.googleapis.com/css2?family=Bangers&family=Comic+Neue:wght@700&family=Luckiest+Guy&display=swap" rel="stylesheet">
<style>
  :root {
    --canvas: #ffffff;
    --ink: #1a1a1a;
    --white: #ffffff;
    --straw-top: #fffbd2;
    --straw-body: #ffb6b6;
    --straw-band: #ff3333;
    --straw-accent: #ff6666;
    --straw-title: #fffbd2;
    --lemon-top: #f8d05a;
    --lemon-body: #f9ef7a;
    --lemon-band: #f59a34;
    --lemon-accent: #fbb731;
    --lemon-title: #ffffff;
  }
  * { box-sizing: border-box; margin: 0; padding: 0; }
  html, body { width: 1200px; height: 1068px; overflow: hidden; background: var(--canvas); }
  .canvas { position: relative; width: 1200px; height: 1068px; }
  .wrapper {
    position: absolute; left: 0; width: 1200px; height: 471px; overflow: hidden;
    background: var(--body);
  }
  .wrapper--strawberry {
    top: 0;
    --top: var(--straw-top); --body: var(--straw-body); --band: var(--straw-band);
    --accent: var(--straw-accent); --title: var(--straw-title);
  }
  .wrapper--lemon {
    top: 597px;
    --top: var(--lemon-top); --body: var(--lemon-body); --band: var(--lemon-band);
    --accent: var(--lemon-accent); --title: var(--lemon-title);
  }
  .top-band { position: absolute; left: 0; top: 0; width: 100%; height: 66px; background: var(--top); }
  .flavor-band { position: absolute; left: 0; bottom: 0; width: 100%; height: 85px; background: var(--band); }
  .tagline {
    position: absolute; left: 322px; top: 12px;
    font-family: "Comic Neue", cursive; font-weight: 700; font-size: 36px;
    color: var(--ink); letter-spacing: 1px;
  }
  .illustration {
    position: absolute; left: 0; top: 28px; width: 330px; height: 443px;
    background: radial-gradient(ellipse at 50% 100%, var(--accent) 0 45%, transparent 46%),
                linear-gradient(180deg, transparent, var(--accent) 160%);
    border-radius: 140px 140px 0 0;
    opacity: .85;
  }
  .bubble { position: absolute; left: 320px; top: 76px; width: 206px; height: 176px; }
  .bubble-text {
    position: absolute; left: 322px; top: 84px; width: 196px; text-align: center;
    font-family: "Bangers", cursive; font-size: 46px; line-height: 42px;
    color: var(--ink); letter-spacing: 1px; transform: skewX(-6deg);
  }
  .brand { position: absolute; left: 524px; top: 194px; width: 660px; height: 180px; }
  .brand text {
    font-family: "Luckiest Guy", cursive; font-size: 190px;
    fill: var(--title); stroke: var(--accent); stroke-width: 22px;
    paint-order: stroke; stroke-linejoin: round;
  }
  .texture {
    position: absolute; left: 476px; bottom: 16px;
    font-family: "Bangers", cursive; font-size: 40px; color: var(--white); letter-spacing: 1px;
  }
  .flavor {
    position: absolute; right: 24px; bottom: 6px;
    font-family: "Bangers", cursive; font-size: 72px; color: var(--white); letter-spacing: 2px;
  }
</style>
</head>
<body>
<main class="canvas">

  <section class="wrapper wrapper--strawberry">
    <div class="top-band"></div>
    <div class="flavor-band"></div>
    <p class="tagline">CHILDREN FRIENDLY</p>
    <div class="illustration" role="img" aria-label="Cartoon rocket launching from a planet among strawberries"></div>
    <svg class="bubble" viewBox="0 0 206 176" aria-hidden="true">
      <path d="M2 2 H196 V94 H150 L182 172 L104 94 H2 Z" fill="var(--accent)" stroke="var(--ink)" stroke-width="2.5" stroke-linejoin="miter"/>
    </svg>
    <p class="bubble-text">20 GM<br>PROTEIN</p>
    <svg class="brand" viewBox="0 0 660 180" aria-label="VELLOW">
      <text x="12" y="164" textLength="636" lengthAdjust="spacingAndGlyphs">VELLOW</text>
    </svg>
    <p class="texture">SMOOTH</p>
    <p class="flavor">STRAWBERRY</p>
  </section>

  <section class="wrapper wrapper--lemon">
    <div class="top-band"></div>
    <div class="flavor-band"></div>
    <p class="tagline">CHILDREN FRIENDLY</p>
    <div class="illustration" role="img" aria-label="Cartoon rocket launching from a planet among lemons"></div>
    <svg class="bubble" viewBox="0 0 206 176" aria-hidden="true">
      <path d="M2 2 H196 V94 H150 L182 172 L104 94 H2 Z" fill="var(--accent)" stroke="var(--ink)" stroke-width="2.5" stroke-linejoin="miter"/>
    </svg>
    <p class="bubble-text">20 GM<br>PROTEIN</p>
    <svg class="brand" viewBox="0 0 660 180" aria-label="VELLOW">
      <text x="22" y="164" textLength="626" lengthAdjust="spacingAndGlyphs">VELLOW</text>
    </svg>
    <p class="texture">CRUNCHY</p>
    <p class="flavor">LEMON</p>
  </section>

</main>
</body>
</html>
```